Whitcombe Framing Works - Card Design

I am looking to use the logo designs that you already did for me to develop a business card. I would like the card to have a black background and be double sided. I want white and green logo and text. I have attached an inspiration photo of a look that I like. I would like to use the Vertical Logo attached to take up the full front side of the card. On the back where I have my name and information, I would like to have the horizontal logo or maybe even just the image of the 'A' and trees without the text. I am open, but I am looking for something clean and simple and I want the green to really pop! Additional files can be found under Design #: 40593216

Target Market(s)

Homeowners

Industry/Entity Type

Construction

Contact Information for Business Card

Name: Marcus Pellow, Title: Project Manager, Phone: 831.555.0147, Email: whitcombeframingworks@mailbarn.net, address: 418 Juniper Ln, Felton, CA 95092, Lic# 2046318

Colors
00AB8E
00BBA5
67D7C9
C6EFE9
E9F9F6

Requirements
Nice to have
• I would like to see the logos that I have already got from SketchHarbor, though I am open to new ones

```html
<!DOCTYPE html>
<html lang="en">
<head>
<meta charset="utf-8">
<title>Whitcombe Framing Works – Business Card</title>
<link href="https://fonts.googleapis.com/css2?family=Poppins:wght@400;600;700&display=swap" rel="stylesheet">
<style>
  :root {
    --backdrop: #d4d5d7;
    --card: #111111;
    --green: #6ab344;
    --white: #ffffff;
    --text: #e8e8e8;
  }
  * { box-sizing: border-box; margin: 0; padding: 0; }
  html, body {
    width: 900px; height: 1200px; overflow: hidden;
    background: var(--backdrop);
    font-family: "Poppins", sans-serif;
  }
  .card {
    position: absolute; left: 120px;
    width: 660px; height: 376px;
    background: var(--card);
  }
  .card--front { top: 203px; display: flex; flex-direction: column; align-items: center; justify-content: center; gap: 18px; }
  .card--back { top: 620px; }

  .brand-mark { width: 44px; height: 44px; background: var(--green); }
  .brand-name {
    color: var(--white); font-weight: 600;
    text-transform: uppercase; letter-spacing: 2px; text-align: center;
  }
  .card--front .brand-name { font-size: 30px; line-height: 1.25; }

  .back-brand { position: absolute; left: 39px; top: 44px; display: flex; align-items: center; gap: 14px; }
  .back-brand .brand-mark { width: 40px; height: 40px; }
  .back-brand .brand-name { font-size: 24px; text-align: left; letter-spacing: 1.5px; }

  .person { position: absolute; left: 34px; top: 196px; }
  .person__name { color: var(--green); font-weight: 700; font-size: 30px; line-height: 1; letter-spacing: 0.5px; text-transform: uppercase; }
  .person__title { color: var(--text); font-size: 15px; letter-spacing: 0.8px; margin-top: 6px; }
  .divider { position: absolute; left: 35px; top: 264px; width: 150px; height: 1px; background: var(--green); }

  .contacts { position: absolute; left: 34px; top: 274px; list-style: none; }
  .contacts li { display: flex; align-items: center; gap: 6px; height: 25px; color: var(--text); font-size: 14px; letter-spacing: 0.4px; white-space: nowrap; }
  .contacts .phone { font-size: 15px; letter-spacing: 2.5px; }
  .contacts svg { width: 15px; height: 15px; fill: var(--green); flex: none; }

  .address { position: absolute; left: 400px; top: 276px; color: var(--text); font-size: 14px; line-height: 24px; letter-spacing: 0.6px; white-space: nowrap; }
</style>
</head>
<body>
  <section class="card card--front">
    <div class="brand-mark"></div>
    <p class="brand-name">Whitcombe<br>Framing Works</p>
  </section>

  <section class="card card--back">
    <div class="back-brand">
      <div class="brand-mark"></div>
      <p class="brand-name">Whitcombe Framing Works</p>
    </div>

    <div class="person">
      <h1 class="person__name">Marcus Pellow</h1>
      <p class="person__title">Project Manager</p>
    </div>
    <div class="divider"></div>

    <ul class="contacts">
      <li class="phone">
        <svg viewBox="0 0 24 24"><path d="M6.6 10.8a15 15 0 0 0 6.6 6.6l2.2-2.2a1 1 0 0 1 1-.25 11.4 11.4 0 0 0 3.6.6 1 1 0 0 1 1 1V20a1 1 0 0 1-1 1A17 17 0 0 1 3 4a1 1 0 0 1 1-1h3.5a1 1 0 0 1 1 1c0 1.25.2 2.45.6 3.6a1 1 0 0 1-.25 1z"/></svg>
        831.555.0147
      </li>
      <li>
        <svg viewBox="0 0 24 24"><path d="M2 5h20v14H2z M2 5l10 8 10-8" fill="none" stroke="#6ab344" stroke-width="2"/><path d="M2 6l10 8 10-8v13H2z"/></svg>
        whitcombeframingworks@mailbarn.net
      </li>
      <li>
        <svg viewBox="0 0 24 24"><circle cx="12" cy="12" r="9" fill="none" stroke="#6ab344" stroke-width="2"/><path d="M3 12h18M12 3c-3 3-3 15 0 18M12 3c3 3 3 15 0 18" fill="none" stroke="#6ab344" stroke-width="1.6"/></svg>
        www.whitcombeframing.net
      </li>
    </ul>

    <p class="address">418 Juniper Ln,<br>Felton, CA 95092<br>Lic# 2046318</p>
  </section>
</body>
</html>
```